Welcome Booklet for Plastic Surgery Patients

I need a welcome booklet for a plastic surgery office. We already have the content and a logo, we just need help putting together a design for the booklet. The book details the types of procedures offered by the doctor (Loriane Whitcombe M.D). Attached is a booklet from another doctor as a reference point (Varnholt Plastic Surgery).
We would like it to be mainly white, gray, black with a little bit of pink as a reflection of the doctors work with Breast Cancer.

Target Market(s)

It is meant to be informative for women seeking Breast Reconstruction who have been diagnosed with breast cancer.

Industry/Entity Type

Plastic

Font styles to use
Other font styles liked:
• century gothic

Colors
7f7f7f
ffffff
1b1b1b
eda3c7

Requirements
Must have
• - Address shown on the back page (we have two locations) -
• 218 S Wexmoor Suite 306 Beverly Hills CA 90211
• 17842 Pellham Street Suite 209 Torrance CA 90503
• - The personal picture of Dr. Whitcombe needs to be on the welcome page
• - Pages 3-7 should have breast reconstruction at the top
• - Page 8 should have face at the top
• - Page 9 Should have body at the top
• - Attached is the image we want for the cover
Nice to have
• -The names of the procedures to stand out
• - For the most part we want a very clean look
• - The logo has been uploaded if there is a good place to place it

```html
<!DOCTYPE html>
<html lang="en">
<head>
<meta charset="utf-8">
<title>Welcome Booklet – Body Procedures Spread</title>
<link href="https://fonts.googleapis.com/css2?family=Questrial&display=swap" rel="stylesheet">
<style>
  :root {
    --canvas: #e4e4e6;
    --page: #f6e4ec;
    --page-edge: #efd6e1;
    --accent: #d98ab6;
    --ribbon: #e49cc2;
    --ink: #3a3a3a;
    --ink-soft: #555557;
    --rule: #b9b2b6;
    --skin-light: #e7c2a4;
    --skin-dark: #b98863;
    --photo-bg: #f1efee;
  }
  * { margin: 0; padding: 0; box-sizing: border-box; }
  html, body { width: 1200px; height: 926px; overflow: hidden; }
  body {
    background: var(--canvas);
    font-family: "Questrial", "Century Gothic", sans-serif;
    color: var(--ink);
    position: relative;
  }
  .spread {
    position: absolute;
    left: 40px; top: 183px;
    width: 1120px; height: 560px;
    background: var(--page);
    box-shadow: 0 14px 30px rgba(0,0,0,.18);
    overflow: hidden;
  }
  .spine {
    position: absolute; left: 559px; top: 0; width: 2px; height: 100%;
    background: linear-gradient(to right, rgba(0,0,0,.06), rgba(0,0,0,.02));
  }

  /* procedure text */
  .procedures { position: absolute; left: 48px; top: 62px; width: 270px; }
  .procedure + .procedure { margin-top: 26px; }
  .procedure-name { font-size: 24px; font-weight: 400; color: var(--ink); margin-bottom: 6px; letter-spacing: .2px; }
  .procedure-copy { font-size: 11.5px; line-height: 1.34; color: var(--ink-soft); }

  /* photo circles */
  .ring, .photo { position: absolute; border-radius: 50%; }
  .hero-ring { left: 350px; top: 6px; width: 470px; height: 470px; background: var(--accent); }
  .hero-photo {
    left: 340px; top: 24px; width: 450px; height: 450px;
    background:
      radial-gradient(ellipse at 45% 30%, var(--skin-light) 0 32%, transparent 55%),
      radial-gradient(ellipse at 62% 62%, #ffffff 0 22%, transparent 40%),
      linear-gradient(100deg, var(--photo-bg) 0%, var(--skin-light) 35%, var(--skin-dark) 60%, var(--photo-bg) 90%);
  }
  .detail-ring { left: 352px; top: 362px; width: 180px; height: 180px; background: var(--accent); }
  .detail-photo {
    left: 360px; top: 366px; width: 170px; height: 170px;
    background:
      radial-gradient(ellipse at 50% 45%, var(--skin-light) 0 25%, transparent 45%),
      linear-gradient(180deg, var(--photo-bg), #ffffff 55%, var(--photo-bg));
  }

  .web {
    position: absolute; left: 470px; top: 500px;
    font-size: 10px; color: var(--ink-soft);
    padding-bottom: 3px; border-bottom: 1px solid var(--rule);
    width: 175px;
  }

  /* contact page */
  .brand { position: absolute; left: 830px; top: 58px; text-align: center; width: 190px; }
  .brand-name { font-size: 13px; color: var(--ink); letter-spacing: .4px; display: flex; align-items: center; justify-content: center; gap: 6px; }
  .brand-dot { width: 9px; height: 9px; border-radius: 50%; background: var(--ink); display: inline-block; }
  .brand-tag { font-size: 7.5px; letter-spacing: 1.6px; color: var(--ink-soft); margin-top: 4px; text-transform: uppercase; }

  .contact { position: absolute; left: 850px; top: 130px; width: 220px; }
  .call-label { font-size: 12.5px; line-height: 1.3; color: var(--ink); }
  .call-number { font-size: 20px; color: var(--ink); margin-top: 2px; letter-spacing: .5px; }
  .office { margin-top: 28px; }
  .office-title { font-size: 15px; color: var(--ink); margin-bottom: 3px; }
  .office-lines { font-size: 10px; line-height: 1.35; color: var(--ink-soft); }

  .footer-rule { position: absolute; height: 1px; background: var(--rule); }
  .footer-left { left: 62px; top: 530px; width: 340px; }
  .footer-right { left: 620px; top: 470px; width: 440px; }
  .ribbon { position: absolute; width: 14px; height: 20px; }
  .ribbon-left { left: 38px; top: 520px; }
  .ribbon-right { left: 1078px; top: 460px; }
</style>
</head>
<body>
  <main class="spread">
    <div class="spine"></div>

    <section class="procedures">
      <article class="procedure">
        <h2 class="procedure-name">Tummy tuck</h2>
        <p class="procedure-copy">Often times pregnancy can weaken the abdominal muscles and can result in excess saggy skin. This procedure is used to rejuvenate the abdomen by repairing abdominal muscle laxity and remove excess skin and fat and is often combined with liposuction for added contour.</p>
      </article>
      <article class="procedure">
        <h2 class="procedure-name">Liposuction</h2>
        <p class="procedure-copy">Whether because of inactivity, less than fantastic dietary habits, or just as an unfortunate and often inescapable part of growing older, many people find themselves developing a bit of extra, unwanted fat here and there. Liposuction is an excellent technique to sculpt the body that you have always dreamed of and attack stubborn areas of fat. Dr. Whitcombe is well known for her liposculpture technique and is one of the best in Beverly Hills.</p>
      </article>
    </section>

    <div class="ring hero-ring"></div>
    <div class="photo hero-photo" role="img" aria-label="Photo of a woman's waist and hips in white briefs, with dashed surgical marking lines on the abdomen and thighs"></div>
    <div class="ring detail-ring"></div>
    <div class="photo detail-photo" role="img" aria-label="Photo of a slim woman's torso in white underwear, side view"></div>

    <p class="web">www.whitcombeplasticsurgery.com</p>

    <div class="brand">
      <div class="brand-name"><span class="brand-dot"></span>Loriane Whitcombe, MD, FACS</div>
      <div class="brand-tag">Beverly Hills Plastic Surgeon</div>
    </div>

    <section class="contact">
      <p class="call-label">CALL US NOW<br>for an appointment:</p>
      <p class="call-number">310.555.0184</p>

      <div class="office">
        <h3 class="office-title">Address 1</h3>
        <p class="office-lines">TORRANCE OFFICE:<br>17842 Pellham St.<br>Suite 209<br>Torrance, CA 90503</p>
      </div>
      <div class="office">
        <h3 class="office-title">Address 2</h3>
        <p class="office-lines">BEVERLY HILLS OFFICE<br>218 S Wexmoor Dr.<br>Ste 306<br>Beverly Hills, CA 90211</p>
      </div>
    </section>

    <div class="footer-rule footer-left"></div>
    <div class="footer-rule footer-right"></div>

    <svg class="ribbon ribbon-left" viewBox="0 0 14 20" aria-hidden="true">
      <path d="M7 8 C2 3 4 0 7 0 C10 0 12 3 7 8 L2 19 L4 20 L7 12 L10 20 L12 19 Z" fill="var(--ribbon)"/>
    </svg>
    <svg class="ribbon ribbon-right" viewBox="0 0 14 20" aria-hidden="true">
      <path d="M7 8 C2 3 4 0 7 0 C10 0 12 3 7 8 L2 19 L4 20 L7 12 L10 20 L12 19 Z" fill="var(--ribbon)"/>
    </svg>
  </main>
</body>
</html>
```